Specialised investor in e-mobility and energy wants business card design

We need a business card design that fits our existing corporate design. <The look and feel must be 'sharp'/'clean', dynamic, communicate momentum, professionalism etc (as one would imagine from a firm in the financial sector). We like the idea of a reverse-side of the card that includes the logo, and the name and contact details on the other. We expect the deliverable to be whatever format might be required to be able to get cards printed directly by a service such as tandor press. Our website is www.orm.capital

```html
<!DOCTYPE html>
<html lang="en">
<head>
<meta charset="utf-8">
<title>Orm Capital – Business Card</title>
<link rel="stylesheet" href="https://fonts.googleapis.com/css2?family=Montserrat:wght@400;500;700;800&display=swap">
<style>
  :root{
    --green-dark:#2f5426;
    --green-light:#7ab342;
    --ink:#2b2b2b;
    --card:#ffffff;
    --backdrop:#ecebe7;
  }
  *{box-sizing:border-box;margin:0;padding:0}
  html,body{width:1200px;height:960px;overflow:hidden}
  body{background:var(--backdrop);font-family:"Montserrat",sans-serif;position:relative}
  .card{
    position:absolute;left:270px;width:660px;height:380px;
    background:var(--card);border-radius:28px;overflow:hidden;
    box-shadow:0 6px 18px rgba(0,0,0,.12);
  }
  .card--front{top:50px}
  .card--back{top:520px}
  .wordmark{
    color:var(--green-dark);font-weight:500;letter-spacing:.01em;white-space:nowrap;
  }
  .card--front .wordmark{
    position:absolute;left:0;right:0;top:0;bottom:0;
    display:flex;align-items:center;justify-content:center;font-size:70px;
  }
  .card__shapes{position:absolute;inset:0}
  .card--back .wordmark{position:absolute;left:125px;top:166px;font-size:36px}
  .divider{position:absolute;left:372px;top:70px;width:2px;height:240px;background:var(--green-light)}
  .details{position:absolute;left:394px;top:70px;color:var(--ink)}
  .details__name{font-weight:800;color:var(--green-light);font-size:21px;letter-spacing:.03em;text-transform:uppercase}
  .details__role{font-size:15px;margin-top:2px}
  .details__company{font-size:15px;color:var(--green-light);margin-top:22px}
  .details__city{font-size:15px;margin-top:2px}
  .contact{list-style:none;margin-top:22px;font-size:15px}
  .contact li{display:flex;align-items:center;gap:8px;margin-bottom:4px}
  .contact svg{width:14px;height:14px;fill:var(--green-dark)}
</style>
</head>
<body>
  <section class="card card--front">
    <div class="wordmark">Orm Capital</div>
  </section>

  <section class="card card--back">
    <svg class="card__shapes" viewBox="0 0 660 380" preserveAspectRatio="none">
      <path d="M0 0 H130 Q40 190 120 380 H0 Z" fill="var(--green-dark)"/>
      <path d="M660 0 V380 H580 Q660 200 600 0 Z" fill="var(--green-light)"/>
    </svg>
    <div class="wordmark">Orm Capital</div>
    <div class="divider"></div>
    <div class="details">
      <p class="details__name">Peter Lindqvist</p>
      <p class="details__role">Managing Director</p>
      <p class="details__company">Orm Capital S.A.</p>
      <p class="details__city">Geneva, Switzerland</p>
      <ul class="contact">
        <li><svg viewBox="0 0 24 24"><path d="M6.6 10.8a15 15 0 0 0 6.6 6.6l2.2-2.2a1 1 0 0 1 1-.25 11.4 11.4 0 0 0 3.6.57 1 1 0 0 1 1 1V20a1 1 0 0 1-1 1A17 17 0 0 1 3 4a1 1 0 0 1 1-1h3.5a1 1 0 0 1 1 1c0 1.25.2 2.45.57 3.57a1 1 0 0 1-.25 1z"/></svg>+41 79 555 0142</li>
        <li><svg viewBox="0 0 24 24"><path d="M2 5h20v14H2z M2 5l10 8 10-8" /></svg>peter@orm.capital</li>
        <li><svg viewBox="0 0 24 24"><circle cx="12" cy="12" r="10"/></svg>www.orm.capital</li>
      </ul>
    </div>
  </section>
</body>
</html>
```